Business cards for a new business: Willow Brook Calm Healing

I would like for the card to include a lotus. The business is a healing practice so I'd like the overall colours to be pink and green and for it to have a soft feel. The name of the practice is
"Willow Brook Calm Healing", which I'd like to be included, as well as the words: "Energetic and spiritual healing to restore health, harmony and wellbeing". Also, my name - Tarik and the number: 5391 6048

Target Market(s)

Everyone interested in personal healing!

Industry/Entity Type

Business

Contact Information for Business Card

As above……..could be single or double-sided
I'd like the font for the name of the practice and my name to be in green and be a flowing, but simple font - elegant.
The background to be a light pink. See below for colours

Colors
f9d9e8
eea4c8
e567a6
d0ebe7
86cfc6
33b7a4

Requirements
Must have
• See above
Nice to have
• See above

```html
<!DOCTYPE html>
<html lang="en">
<head>
<meta charset="utf-8">
<title>Willow Brook Calm Healing — Business Card</title>
<link href="https://fonts.googleapis.com/css2?family=Gelasio:wght@700&family=Great+Vibes&family=Allura&family=PT+Sans&display=swap" rel="stylesheet">
<style>
  :root {
    --page: #ffffff;
    --card-pink: #f497c0;
    --card-pink-mid: #e07fab;
    --card-plum: #9c3c69;
    --card-plum-deep: #5e1236;
    --brand-green: #3f8a3d;
    --ink: #1a1a1a;
    --petal-white: #eef3ea;
    --petal-blush: #f6c3dc;
    --petal-pink: #ec6aa9;
    --petal-green: #c9e8b6;
    --leaf-green: #5f9e3a;
  }
  * { box-sizing: border-box; margin: 0; padding: 0; }
  html, body {
    width: 1200px;
    height: 827px;
    overflow: hidden;
    background: var(--page);
  }
  .canvas {
    position: relative;
    width: 1200px;
    height: 827px;
    background: var(--page);
  }
  .business-card {
    position: absolute;
    left: 105px;
    top: 119px;
    width: 975px;
    height: 502px;
    overflow: hidden;
    background: linear-gradient(180deg,
      var(--card-pink) 0%,
      var(--card-pink) 62%,
      var(--card-pink-mid) 78%,
      var(--card-plum) 92%,
      var(--card-plum-deep) 100%);
  }
  .lotus-art {
    position: absolute;
    opacity: 0.9;
  }
  .lotus-art--left {
    left: 0;
    top: 176px;
    width: 330px;
    height: 326px;
    border-top-right-radius: 60% 50%;
    background: linear-gradient(180deg,
      var(--petal-pink) 0%,
      var(--petal-blush) 25%,
      var(--petal-white) 55%,
      var(--petal-green) 85%,
      var(--leaf-green) 100%);
  }
  .lotus-art--right {
    left: 706px;
    top: 64px;
    width: 269px;
    height: 438px;
    border-top-left-radius: 70% 40%;
    background: linear-gradient(180deg,
      var(--petal-pink) 0%,
      var(--petal-blush) 30%,
      var(--petal-white) 60%,
      var(--petal-green) 88%,
      var(--leaf-green) 100%);
  }
  .card-content {
    position: absolute;
    inset: 0;
    text-align: center;
  }
  .practice-name {
    position: absolute;
    left: 0;
    right: 0;
    top: 80px;
    font-family: "Gelasio", Georgia, serif;
    font-weight: 700;
    font-size: 33px;
    word-spacing: 5px;
    color: var(--brand-green);
    line-height: 1;
  }
  .tagline-script {
    position: absolute;
    left: 0;
    right: 0;
    top: 132px;
    font-family: "Great Vibes", cursive;
    font-size: 42px;
    word-spacing: 6px;
    color: var(--ink);
    line-height: 1;
  }
  .tagline {
    position: absolute;
    left: 0;
    right: 0;
    font-family: "PT Sans", Arial, sans-serif;
    font-size: 16px;
    color: var(--ink);
    word-spacing: 3px;
    line-height: 1;
  }
  .tagline--first { top: 187px; }
  .tagline--second { top: 217px; }
  .practitioner-name {
    position: absolute;
    left: 0;
    right: 0;
    top: 258px;
    font-family: "Allura", cursive;
    font-size: 122px;
    color: var(--brand-green);
    line-height: 1;
  }
  .phone {
    position: absolute;
    left: 0;
    right: 0;
    top: 398px;
    font-family: "PT Sans", Arial, sans-serif;
    font-size: 16px;
    color: var(--ink);
    line-height: 1;
  }
</style>
</head>
<body>
  <main class="canvas">
    <section class="business-card">
      <div class="lotus-art lotus-art--left" role="img" aria-label="Illustration of a white and pink lotus flower with golden stamens and a green leaf"></div>
      <div class="lotus-art lotus-art--right" role="img" aria-label="Illustration of an open lotus flower and a pink lotus bud with soft translucent petals and sparkles"></div>

      <div class="card-content">
        <h1 class="practice-name">Willow Brook Calm Healing</h1>
        <p class="tagline-script">Energetic &amp; spiritual</p>
        <p class="tagline tagline--first">HEALING TO RESTORE</p>
        <p class="tagline tagline--second">HEALTH, HARMONY &amp; WELLBEING</p>
        <p class="practitioner-name">Tarik</p>
        <p class="phone">(02) 5391 6048</p>
      </div>
    </section>
  </main>
</body>
</html>
```